Cork Lantern website design elements

Company: Cork Lantern
Business: Wine website (selling wine online)
www.corklantern-demo.com.au
Please note that this is an initial project, ongoing design work will be required after this project.
Design requirement
Note: Full website design not required, only specific elements to enhance current design.
- Must work with existing logo and wood background (do not change site background)
- Must work with a orange (please improve current orange colour) and blue colour (blue colour in attachments)
- Pictures of wine bottles or wine glasses are not to be used in design elements.
I currently have an existing design which I would like certain elements designed for. Design elements must work with responsive functionality.
I am trying to achieve a modern retro feel of the website, please refer to the below websites as examples that I am trying to look like.
- https://au.brisktrimhouse-demo.com/
- http://www.kestrelmarlow-demo.com/italian/australia/home
- http://www.tangerinefizz-demo.co.uk/
- http://www.codeharbour-demo.org.nz/13/
As mentioned the site is already built and I need certain elements to work with what is already there. All elements must work with current logo and wood panel background.
I require the following elements
• Menu bar (must be the orange)
• Home page promo slider (Text, this weeks special etc)
• 2x homepage promo tabs buttons (Join the lantern club, what's in the box deal)
• 4x Homepage navigation tabs (Red wine, White wine, Sparkling, Pre mixed cases)
• Add to cart button
• Product image backdrop (can be wider than current examples)
o I would like the backdrops to be a different colour scheme to each other e.g red wine will habe red colour, white will have a cream colour, etc)
o I would prefer a close up of the product, does not need to be full view
Please refer to attachments for elements that I like and would like to mimic.
Colour scheme
- Use existing orange (please suggest if you think of a better tone)
- Secondary colour light baby blue (suggest best options)
- Please advise of other colours needed
Design elements to be provided in jog and raw design format.
This project will require ongoing work.
I will provide access details to site upon request.
Please contact me if you have any questions.
Tobias
Cork Lantern

```html
<!DOCTYPE html>
<html lang="en">
<head>
<meta charset="utf-8">
<title>Cork Lantern</title>
<link rel="stylesheet" href="https://fonts.googleapis.com/css2?family=Bebas+Neue&family=Open+Sans:wght@400;600&display=swap">
<style>
  :root {
    --wood-light: #9a6a40;
    --wood-dark: #6b4225;
    --orange: #e8602a;
    --orange-dark: #c94d1c;
    --teal: #3fb8c4;
    --teal-soft: #6ac5cc;
    --teal-band: #acdcdb;
    --cream: #f8f3e6;
    --card: #ffffff;
    --frame: #c9b08f;
    --ink: #2d2a26;
    --body: #3a3530;
    --white: #ffffff;
  }
  * { box-sizing: border-box; margin: 0; padding: 0; }
  html, body { width: 1179px; height: 1200px; overflow: hidden; }
  body { font-family: "Open Sans", sans-serif; color: var(--body); }
  .page { position: relative; width: 1179px; height: 1200px; overflow: hidden; }
  .wood-backdrop {
    position: absolute; inset: 0;
    background: linear-gradient(90deg, var(--wood-dark), var(--wood-light) 30%, var(--wood-dark) 55%, var(--wood-light) 80%, var(--wood-dark));
  }
  .brand {
    position: absolute; left: 90px; top: 38px;
    display: flex; align-items: center; gap: 10px;
    font-family: "Bebas Neue", sans-serif; font-size: 40px; color: var(--white); letter-spacing: 1px;
  }
  .brand-dot { width: 14px; height: 14px; border-radius: 50%; background: var(--orange); }
  .search { position: absolute; left: 807px; top: 68px; width: 283px; height: 36px; display: flex; }
  .search-field { flex: 1; background: var(--white); font-size: 13px; color: #9a9a9a; padding: 9px 14px; }
  .search-button { width: 37px; background: var(--teal); display: flex; align-items: center; justify-content: center; }
  .main-nav {
    position: absolute; left: 88px; top: 122px; width: 1002px; height: 47px;
    background: var(--orange); border-top: 3px solid var(--orange-dark);
    box-shadow: inset 0 3px 0 #f07a45;
    display: flex; align-items: center; padding-left: 22px; gap: 41px;
  }
  .main-nav a { font-family: "Bebas Neue", sans-serif; font-size: 21px; color: var(--white); text-decoration: none; letter-spacing: 0.3px; }
  .panel { position: absolute; left: 88px; top: 169px; width: 1002px; height: 1031px; background: var(--cream); }
  .slider-frame { position: absolute; left: 22px; top: 16px; width: 959px; height: 357px; background: var(--frame); }
  .slider-mat { position: absolute; left: 15px; top: 17px; width: 929px; height: 329px; background: var(--white); box-shadow: 0 1px 3px rgba(0,0,0,.25); }
  .slider { position: absolute; left: 8px; top: 7px; width: 914px; height: 316px; background: radial-gradient(ellipse at 60% 40%, #4fc6d0, var(--teal) 70%, #2fa3b0); overflow: hidden; }
  .slider-title { position: absolute; left: 38px; top: 70px; font-family: "Bebas Neue", sans-serif; font-size: 64px; line-height: 56px; color: var(--white); letter-spacing: 1px; }
  .hat-art { position: absolute; left: 322px; top: 58px; width: 134px; height: 92px; border-radius: 50% 50% 20% 20%; background: linear-gradient(#d62a2a, #b81f1f); }
  .price-badge { position: absolute; left: 295px; top: 138px; }
  .price-text { position: absolute; left: 295px; top: 152px; width: 140px; text-align: center; color: var(--white); }
  .price-text .amount { font-family: "Bebas Neue", sans-serif; font-size: 46px; line-height: 44px; }
  .price-text .detail { font-size: 13px; line-height: 16px; }
  .bubble { position: absolute; left: 480px; top: 72px; }
  .bubble-text { position: absolute; left: 484px; top: 102px; width: 210px; text-align: center; font-family: "Bebas Neue", sans-serif; font-size: 25px; line-height: 28px; color: var(--teal); }
  .santa-art { position: absolute; left: 672px; top: 16px; width: 206px; height: 300px; border-radius: 45% 45% 10% 10%; background: linear-gradient(160deg, #c98a55 0%, #d5473a 55%, #b9302a 100%); }
  .cards { position: absolute; left: 22px; top: 404px; width: 961px; height: 283px; }
  .card { position: absolute; top: 17px; width: 313px; height: 266px; background: linear-gradient(#fff 70%, #f0efed); box-shadow: 0 1px 2px rgba(0,0,0,.2); }
  .card-ribbon { position: absolute; left: 14px; top: -17px; }
  .card-title { position: absolute; left: 44px; top: -12px; font-family: "Bebas Neue", sans-serif; font-size: 23px; color: var(--white); }
  .card-text { position: absolute; left: 22px; top: 44px; width: 276px; font-size: 13px; line-height: 23px; color: var(--body); }
  .card-link { position: absolute; left: 22px; top: 233px; font-size: 12px; color: var(--orange); text-decoration: none; }
  .band { position: absolute; left: 22px; width: 978px; height: 17px; }
  .footer-col { position: absolute; top: 759px; }
  .footer-heading { font-family: "Bebas Neue", sans-serif; font-size: 23px; color: var(--ink); margin-bottom: 8px; }
  .footer-text { font-size: 12px; line-height: 23px; color: var(--body); width: 290px; }
  .tip-list { list-style: none; }
  .tip-list li { display: flex; align-items: center; gap: 8px; font-size: 12px; height: 32px; }
  .tip-number { width: 20px; height: 20px; border-radius: 50%; background: var(--orange); color: var(--white); font-size: 11px; font-weight: 600; display: flex; align-items: center; justify-content: center; }
  .feature-list { list-style: none; }
  .feature-list li { font-size: 12px; line-height: 30px; }
  .legal-links { position: absolute; left: 22px; top: 975px; font-size: 11px; color: var(--body); }
  .copyright { position: absolute; left: 22px; top: 998px; font-size: 11px; color: var(--body); }
  .social { position: absolute; left: 892px; top: 970px; display: flex; gap: 4px; }
  .social span { width: 28px; height: 28px; border-radius: 50%; background: var(--teal); }
</style>
</head>
<body>
<div class="page">
  <div class="wood-backdrop" role="img" aria-label="Wood panel background"></div>

  <div class="brand"><span class="brand-dot"></span>Cork Lantern</div>

  <div class="search">
    <div class="search-field">Search entire store here</div>
    <div class="search-button">
      <svg width="20" height="20" viewBox="0 0 20 20"><circle cx="8" cy="8" r="6" fill="none" stroke="#fff" stroke-width="2.2"/><line x1="12.5" y1="12.5" x2="18" y2="18" stroke="#fff" stroke-width="2.4" stroke-linecap="round"/></svg>
    </div>
  </div>

  <nav class="main-nav">
    <a href="#">Home</a><a href="#">Red Wine</a><a href="#">White Wine</a><a href="#">Sparkling</a><a href="#">Pre Mixed Cases</a><a href="#">Build by Variety</a>
  </nav>

  <main class="panel">
    <section class="slider-frame">
      <div class="slider-mat">
        <div class="slider">
          <h1 class="slider-title">Christmas<br>Mystery<br>Box</h1>
          <div class="hat-art" role="img" aria-label="Santa hat illustration"></div>
          <svg class="price-badge" width="140" height="140" viewBox="0 0 140 140">
            <polygon fill="#e8602a" points="70,0 79,16 95,5 98,24 117,19 113,38 132,40 121,56 138,66 122,77 132,94 113,96 117,115 98,111 95,130 79,120 70,138 61,120 45,130 42,111 23,115 27,96 8,94 18,77 2,66 19,56 8,40 27,38 23,19 42,24 45,5 61,16"/>
          </svg>
          <div class="price-text"><div class="amount">$149</div><div class="detail">Mixed 6<br>bottle case</div></div>
          <svg class="bubble" width="220" height="160" viewBox="0 0 220 160">
            <ellipse cx="110" cy="62" rx="108" ry="60" fill="#fff"/>
            <path d="M90 110 L62 152 L128 116 Z" fill="#fff"/>
          </svg>
          <div class="bubble-text">Free Delivery*<br>Click to order now</div>
          <div class="santa-art" role="img" aria-label="Santa carrying a sack of wine illustration"></div>
        </div>
      </div>
    </section>

    <section class="cards">
      <article class="card" style="left:0">
        <svg class="card-ribbon" width="288" height="42" viewBox="0 0 288 42"><polygon points="0,0 288,0 278,21 288,42 0,42 10,21" fill="#6ac5cc"/><polyline points="12,4 6,21 12,38" fill="none" stroke="#fff" stroke-width="1.5"/><polyline points="276,4 282,21 276,38" fill="none" stroke="#fff" stroke-width="1.5"/></svg>
        <h2 class="card-title">Red Wine</h2>
        <p class="card-text">Lorem Ipsum is simply dummy text of the printing and typesetting industry. Lorem Ipsum has been the industry's standard dummy text ever since the 1500s, when an unknown printer took a galley of type and scrambled it to make a type specimen book. It has survived not only five centuries, but also the leap into electronic.</p>
        <a class="card-link" href="#">SEE ALL RED WINES</a>
      </article>
      <article class="card" style="left:330px">
        <svg class="card-ribbon" width="288" height="42" viewBox="0 0 288 42"><polygon points="0,0 288,0 278,21 288,42 0,42 10,21" fill="#6ac5cc"/><polyline points="12,4 6,21 12,38" fill="none" stroke="#fff" stroke-width="1.5"/><polyline points="276,4 282,21 276,38" fill="none" stroke="#fff" stroke-width="1.5"/></svg>
        <h2 class="card-title">White Wine</h2>
        <p class="card-text">Lorem Ipsum is simply dummy text of the printing and typesetting industry. Lorem Ipsum has been the industry's standard dummy text ever since the 1500s, when an unknown printer took a galley of type and scrambled it to make a type specimen book. It has survived not only five centuries, but also the leap into electronic.</p>
        <a class="card-link" href="#">SEE ALL RED WINES</a>
      </article>
      <article class="card" style="left:648px">
        <svg class="card-ribbon" width="288" height="42" viewBox="0 0 288 42"><polygon points="0,0 288,0 278,21 288,42 0,42 10,21" fill="#6ac5cc"/><polyline points="12,4 6,21 12,38" fill="none" stroke="#fff" stroke-width="1.5"/><polyline points="276,4 282,21 276,38" fill="none" stroke="#fff" stroke-width="1.5"/></svg>
        <h2 class="card-title">Sparkling</h2>
        <p class="card-text">Lorem Ipsum is simply dummy text of the printing and typesetting industry. Lorem Ipsum has been the industry's standard dummy text ever since the 1500s, when an unknown printer took a galley of type and scrambled it to make a type specimen book. It has survived not only five centuries, but also the leap into electronic.</p>
        <a class="card-link" href="#">SEE ALL RED WINES</a>
      </article>
    </section>

    <svg class="band" style="top:709px" viewBox="0 0 978 17" preserveAspectRatio="none"><polygon points="0,0 978,0 970,8.5 978,17 0,17 8,8.5" fill="#acdcdb"/></svg>

    <div class="footer-col" style="left:23px">
      <h3 class="footer-heading">Cork Lantern</h3>
      <p class="footer-text">Cork Lantern - ABN 00 000 000 000 - Liquor licence No. 00000000 PO Box 0000, Harbourvale ACT 2900<br>email: info@corklantern-demo.com.au<br>IT IS AN OFFENCE TO SUPPLY ALCOHOL TO A PERSON UNDER THE AGE OF 18 YEARS PENALTIES APPLY</p>
    </div>
    <div class="footer-col" style="left:346px">
      <h3 class="footer-heading">Tobias to Suggest</h3>
      <ol class="tip-list">
        <li><span class="tip-number">1</span>Unlimited colors, dozens of customizable elements</li>
        <li><span class="tip-number">2</span>Customizable responsive layout based on fluid grid</li>
        <li><span class="tip-number">3</span>50+ placeholders to display custom content</li>
        <li><span class="tip-number">4</span>Create your custom sub-themes (variants)</li>
      </ol>
    </div>
    <div class="footer-col" style="left:675px">
      <h3 class="footer-heading">Theme Features</h3>
      <ul class="feature-list">
        <li>Theme Features</li><li>Typography</li><li>Sample Link</li><li>Meat Our Best Partners</li><li>Our Other Projects</li>
      </ul>
    </div>

    <svg class="band" style="top:944px" viewBox="0 0 978 17" preserveAspectRatio="none"><polygon points="0,0 978,0 970,8.5 978,17 0,17 8,8.5" fill="#acdcdb"/></svg>

    <p class="legal-links">About Us &nbsp;|&nbsp; Shipping and Delivery &nbsp;|&nbsp; Refund Policy &nbsp;|&nbsp; Customer Service</p>
    <p class="copyright">© 2013 Cork Lantern. All Rights Reserved.</p>
    <div class="social" aria-label="Social links"><span></span><span></span><span></span></div>
  </main>
</div>
</body>
</html>
```